Social Media Cover and Profile

We already have our own logo. We just need a fresh design on our social media pages. We are not happy with our current designs. We would like to incorporate our YIKE billboard and the colors are blue (#05143f) and white. You can also incorporate silver as well. We are a family law office (Divorce and Custody) We no longer want to incorporate the Spire of Dunvale photo that we are currently using. You can look at our Facebook page; The Law Office of Miles T. Hadley.

Target Market(s)

Potential Clients

Industry/Entity Type

Family Law

Logo Text

Our Logo Is The Law Office of Miles T. Hadley with the Sheild

Requirements
Must have
• Text to include:
Central Pennslyvania's Premier Family Law Firm

Ability to be resized to and used as all images in social media, including but not limited to: Youtube Channel art, Facebook Cover and Profile.
Nice to have
• Darker color but we are open to "bright" ideas.

```html
<!DOCTYPE html>
<html lang="en">
<head>
<meta charset="utf-8">
<title>Miles T. Hadley – Social Cover</title>
<link rel="stylesheet" href="https://fonts.googleapis.com/css2?family=Tinos&display=swap">
<style>
  :root {
    --navy: #05143f;
    --white: #ffffff;
    --silver: #9a9b9e;
  }
  html, body {
    margin: 0;
    padding: 0;
    width: 1200px;
    height: 457px;
    overflow: hidden;
    background: var(--navy);
  }
  .cover {
    position: relative;
    width: 1200px;
    height: 457px;
    background: var(--navy);
    overflow: hidden;
    font-family: "Tinos", "Times New Roman", serif;
    font-weight: 400;
  }
  .cover__wave {
    position: absolute;
    inset: 0;
    width: 1200px;
    height: 457px;
  }
  .firm-name {
    position: absolute;
    left: 22px;
    top: 62px;
    margin: 0;
    color: var(--white);
    font-weight: 400;
    text-transform: uppercase;
    line-height: 1;
    letter-spacing: 1px;
  }
  .firm-name__lead {
    display: block;
    font-size: 19px;
  }
  .firm-name__main {
    display: block;
    font-size: 38px;
    margin-top: 4px;
  }
  .billboard-mark {
    position: absolute;
    right: 112px;
    top: 28px;
    margin: 0;
    color: var(--silver);
    font-size: 80px;
    font-weight: 400;
    line-height: 1;
    letter-spacing: 4px;
  }
  .tagline {
    position: absolute;
    right: 62px;
    top: 266px;
    margin: 0;
    color: var(--white);
    font-size: 47px;
    font-weight: 400;
    line-height: 1;
    white-space: nowrap;
  }
</style>
</head>
<body>
  <main class="cover">
    <svg class="cover__wave" viewBox="0 0 1200 457" aria-hidden="true">
      <path d="M70,0 C380,8 640,70 880,128 C1020,162 1110,178 1150,158 C1188,138 1198,95 1200,60 L1200,0 Z" fill="var(--white)"/>
    </svg>

    <h1 class="firm-name">
      <span class="firm-name__lead">The Law Office of</span>
      <span class="firm-name__main">Miles T. Hadley</span>
    </h1>

    <p class="billboard-mark">YIKE</p>

    <p class="tagline">Central Pennslyvania's Premier Family Law Firm</p>
  </main>
</body>
</html>
```